Luxury Business Card Design for High-End Window Treatments

Gilded Vantages
Custom Plantation Shutters & Architectural Shading Systems

⸻

BACK

Daniel Forsythe
Owner

Custom Interior & Exterior Window Treatments

919-482-7034
gildedvantages.com

I have included a picture that I’m hoping we can use on the back, but I’m also wondering if you can get rid of the ladder? Should we get rid of shutters , shades and blinds underneath Gilded Vantages?

Target Market(s)

High-end residential homeowners, custom home builders, architects, interior designers, and luxury renovation clients seeking premium plantation shutters and motorized architectural shading systems.

Industry/Entity Type

Custom Window treatments

Contact Information for Business Card

Front Gilded Vantages Custom Plantation Shutters Motorized Architectural Shading Systems BACK Daniel Forsythe Owner 919-482-7034 GildedVantages.com Custom Interior & Exterior Window Treatments By Appointment

Requirements
Nice to have
• Not 100% sure on nice to halves or the color but you can definitely check out my website to get a better understanding of what I’m trying to do

```html
<!DOCTYPE html>
<html lang="en">
<head>
<meta charset="utf-8">
<title>Gilded Vantages – Business Card</title>
<link rel="stylesheet" href="https://fonts.googleapis.com/css2?family=Open+Sans:wght@400;700;800&display=swap">
<style>
  :root {
    --page: #1b1b1b;
    --card-black: #181818;
    --gold-dark: #b07a22;
    --gold: #d9a93d;
    --gold-light: #f4d87a;
    --gold-copper: #c8711c;
    --ink: #111111;
    --white: #f4f4f4;
    --sky: #4d8fdc;
    --shade: #2c2f36;
    --stone: #6b5a4a;
  }
  * { box-sizing: border-box; margin: 0; padding: 0; }
  html, body {
    width: 1200px; height: 963px; overflow: hidden;
    background: var(--page);
    font-family: "Open Sans", sans-serif;
  }
  .sheet {
    width: 1200px; height: 963px;
    display: flex; flex-direction: column; align-items: center; justify-content: center;
    gap: 36px;
  }
  .card {
    position: relative;
    width: 760px; height: 434px;
    box-shadow: 0 10px 30px rgba(0,0,0,.5);
    overflow: hidden;
  }

  /* ---------- Contact side ---------- */
  .card--contact { background: var(--card-black); }
  .card--contact .frame { position: absolute; inset: 0; }
  .brand {
    position: absolute; left: 70px; top: 150px; width: 300px;
    text-align: center;
  }
  .brand__name {
    font-weight: 400; font-size: 42px; line-height: 1.15;
    color: var(--gold);
  }
  .divider {
    position: absolute; left: 405px; top: 120px; width: 1.5px; height: 160px;
    background: var(--gold);
  }
  .contact { position: absolute; left: 440px; top: 135px; }
  .contact__name {
    font-weight: 800; font-size: 25px; letter-spacing: .5px;
    color: var(--gold-light);
    text-transform: uppercase;
  }
  .contact__role { font-size: 17px; color: var(--white); margin-top: -2px; }
  .contact__list { list-style: none; margin-top: 26px; }
  .contact__item {
    display: flex; align-items: center; gap: 8px;
    font-size: 19px; color: var(--white); line-height: 1.5;
  }
  .contact__icon { width: 16px; height: 16px; flex: none; }
  .tagline {
    position: absolute; left: 72px; bottom: 20px;
    font-size: 19px; color: var(--white); letter-spacing: .2px;
  }

  /* ---------- Photo side ---------- */
  .card--photo {
    background: linear-gradient(120deg, var(--gold-dark) 0%, var(--gold-light) 30%, var(--gold-copper) 55%, var(--gold-light) 78%, var(--gold) 100%);
  }
  .card--photo .frame { position: absolute; inset: 0; }
  .photo {
    position: absolute; left: 42px; top: 34px; right: 42px; bottom: 70px;
    background: linear-gradient(180deg, var(--sky) 0%, #8fb8e6 18%, var(--shade) 35%, #3a3a3e 65%, var(--stone) 100%);
  }
  .photo-caption {
    position: absolute; left: 62px; bottom: 30px;
    font-weight: 700; font-size: 15.5px; color: var(--ink);
  }
</style>
</head>
<body>
<main class="sheet">

  <section class="card card--contact" aria-label="Card back with contact details">
    <svg class="frame" width="760" height="434" viewBox="0 0 760 434" aria-hidden="true">
      <polyline points="60,405 30,405 30,30 730,30 730,405 505,405" fill="none" stroke="#d9a93d" stroke-width="1.5"/>
    </svg>
    <div class="brand">
      <p class="brand__name">Gilded Vantages</p>
    </div>
    <div class="divider"></div>
    <div class="contact">
      <h1 class="contact__name">Daniel Forsythe</h1>
      <p class="contact__role">Owner</p>
      <ul class="contact__list">
        <li class="contact__item">
          <svg class="contact__icon" viewBox="0 0 16 16" aria-hidden="true"><circle cx="8" cy="8" r="8" fill="#d9a93d"/><path d="M5 4.5c.6-.5 1.3-.3 1.6.3l.6 1.2c.2.4 0 .8-.3 1l-.5.4c.4.9 1.2 1.7 2.1 2.1l.4-.5c.3-.3.7-.4 1-.2l1.2.6c.6.3.7 1 .3 1.6-.5.6-1.3.9-2 .6C7.2 10.8 5.2 8.8 4.4 6.6c-.3-.7 0-1.5.6-2.1z" fill="#181818"/></svg>
          919-482-7034
        </li>
        <li class="contact__item">
          <svg class="contact__icon" viewBox="0 0 16 16" aria-hidden="true"><circle cx="8" cy="8" r="8" fill="#d9a93d"/><g fill="none" stroke="#181818" stroke-width="1"><circle cx="8" cy="8" r="5"/><ellipse cx="8" cy="8" rx="2.2" ry="5"/><line x1="3" y1="8" x2="13" y2="8"/></g></svg>
          gildedvantages.com
        </li>
      </ul>
    </div>
    <p class="tagline">Custom Interior &amp; Exterior Window Treatments</p>
  </section>

  <section class="card card--photo" aria-label="Card front with photo">
    <svg class="frame" width="760" height="434" viewBox="0 0 760 434" aria-hidden="true">
      <polyline points="50,405 28,405 28,20 732,20 732,405 705,405" fill="none" stroke="#111111" stroke-width="1.5"/>
    </svg>
    <div class="photo" role="img" aria-label="Photo of a house porch fitted with dark motorized exterior shades under a blue sky with pine trees"></div>
    <p class="photo-caption">Custom Plantation Shutters &amp; Motorized Architectural Shading Systems</p>
  </section>

</main>
</body>
</html>
```